FinTech company looking to revamp and expand client-facing interface for our financial models

Halvern Ledgerworks currently has a very simple website that allows clients to interact with our financial models. We are looking to completely redesign the current site and add several extra pages to provide extra functionality. We want the design to have a modern, slick feel, that will work on both a desktop or a tablet. It should be straightforward for clients to move between different pages at any time, and clear from the layout how to interact with the more advanced features. We have included screenshots of existing pages in the attached design brief, as well as sketches of the functionality required by the new pages, but can't provide a direct link to the current site.
Target Market(s)
Professional investors that will be paying to access the interface
Industry/Entity Type
Finance
Number of Pages Required
4 page
Colors
Designer to choose colors to be used in the design.
Look and feel
Each slider illustrates characteristics of the customer's brand and the style your logo design should communicate.

```html
<!DOCTYPE html>
<html lang="en">
<head>
<meta charset="utf-8">
<title>Halvern Ledgerworks · Models</title>
<link href="https://fonts.googleapis.com/css2?family=Montserrat:wght@600;700&family=Roboto+Condensed:wght@400;500&family=Open+Sans:wght@600;700&display=swap" rel="stylesheet">
<style>
  :root {
    --ink: #111;
    --navy: #0d2a40;
    --muted: #8a8a8a;
    --tab: #e4e4e4;
    --line: #d6d6d6;
    --row: #fcfcfc;
    --chart-bg: #1f1f1f;
    --chart-grid: #3a3a3a;
    --gain: #16a31a;
    --loss: #e0141e;
    --dark: #1c1c1c;
  }
  * { box-sizing: border-box; margin: 0; padding: 0; }
  html, body { width: 1200px; height: 750px; overflow: hidden; background: #fff; }
  body { position: relative; color: var(--ink); font-family: "Roboto Condensed", sans-serif; }

  .horizon { position: absolute; top: 27px; left: 15px; display: flex; gap: 0; font-family: "Montserrat", sans-serif; font-weight: 700; font-size: 15px; }
  .horizon__item { display: flex; align-items: center; gap: 8px; width: 100px; color: #333; }
  .horizon__item::before { content: ""; width: 9px; height: 9px; border-radius: 50%; background: var(--muted); }
  .horizon__item--active { color: var(--navy); }
  .horizon__item--active::before { background: #000; }

  .pages { position: absolute; top: 28px; left: 673px; font-family: "Montserrat", sans-serif; font-weight: 600; font-size: 16.5px; color: #222; }
  .pages a { position: absolute; color: inherit; text-decoration: none; white-space: nowrap; }
  .pages .pages__link--active { color: var(--navy); }
  .pages .pages__link--active::after { content: ""; position: absolute; left: -3px; right: -6px; top: 23px; height: 2px; background: var(--navy); }

  .model-panel { position: absolute; left: 108px; top: 262px; width: 387px; }
  .model-tabs { display: flex; height: 42px; background: var(--tab); }
  .model-tab { width: 188px; padding: 13px 0 0 16px; font-size: 13px; font-weight: 500; }
  .model-tab--current { border: 1px solid #aaa; background: #e1e1e1; }
  .model-tab + .model-tab { padding-left: 20px; }
  .model-row { position: relative; display: flex; align-items: center; border-bottom: 1px solid var(--line); background: var(--row); padding-left: 16px; font-size: 9px; font-weight: 500; }
  .model-row__value { position: absolute; left: 209px; font-weight: 400; }
  .model-row--title { height: 41px; font-size: 13px; font-weight: 400; }
  .badge { position: absolute; right: 11px; top: 15px; width: 32px; height: 11px; border: 1px solid #555; border-radius: 6px; font-size: 4.5px; text-align: center; line-height: 9px; color: #333; }
  .gain { color: var(--gain); }
  .loss { color: var(--loss); }
  .run { position: absolute; right: 2px; top: 271px; width: 43px; height: 21px; background: var(--dark); color: #fff; border: 0; border-radius: 3px; font: 400 9px "Roboto Condensed", sans-serif; }

  .pnl-label { position: absolute; left: 563px; top: 368px; transform: rotate(-90deg); font: 700 13px "Open Sans", sans-serif; color: #333; }
  .pnl-chart { position: absolute; left: 605px; top: 260px; width: 487px; height: 232px; border-radius: 6px; overflow: hidden; background: var(--chart-bg); }
  .year { position: absolute; top: 507px; font: 700 11.5px "Open Sans", sans-serif; color: #444; letter-spacing: .5px; }

  .stats { position: absolute; left: 605px; top: 532px; width: 488px; font-family: "Open Sans", sans-serif; }
  .stats__head { height: 26px; background: var(--dark); color: #fff; border-radius: 4px; font-weight: 700; font-size: 11px; padding: 6px 0 0 24px; }
  .stats__table { margin-top: 5px; border: 1px solid var(--line); border-radius: 3px; }
  .stats__row { position: relative; height: 44px; display: flex; align-items: center; padding-left: 24px; font-size: 10.5px; font-weight: 700; border-bottom: 1px solid var(--line); }
  .stats__row:last-child { border-bottom: 0; }
  .stats__value { position: absolute; left: 407px; transform: translateX(-50%); font-size: 13px; top: 9px; }
</style>
</head>
<body>
  <nav class="horizon" aria-label="Horizon">
    <span class="horizon__item horizon__item--active">250D</span>
    <span class="horizon__item">83D</span>
    <span class="horizon__item">24D</span>
  </nav>

  <nav class="pages" aria-label="Pages">
    <a class="pages__link--active" href="#" style="left:0">models</a>
    <a href="#" style="left:145px">sensitivities</a>
    <a href="#" style="left:329px">favourites</a>
  </nav>

  <section class="model-panel">
    <div class="model-tabs">
      <div class="model-tab model-tab--current">Model 1</div>
      <div class="model-tab">Model 2</div>
    </div>
    <div class="model-row model-row--title">Model : Model name <span class="badge">Selected</span></div>
    <div class="model-row" style="height:43px">Parameters</div>
    <div class="model-row" style="height:40px">Entry <span class="model-row__value gain">0.5</span></div>
    <div class="model-row" style="height:43px">Exit <span class="model-row__value loss">-0.3</span></div>
    <div class="model-row" style="height:41px">Lookback <span class="model-row__value gain">5</span></div>
    <button class="run">Run</button>
  </section>

  <div class="pnl-label">PNL</div>
  <svg class="pnl-chart" viewBox="0 0 584 279" preserveAspectRatio="none" aria-label="PNL line chart 2014 to 2019">
    <defs>
      <linearGradient id="area" x1="0" y1="0" x2="0" y2="1">
        <stop offset="0" stop-color="#4a4a4a"/>
        <stop offset="1" stop-color="#2b2b2b"/>
      </linearGradient>
    </defs>
    <g stroke="var(--chart-grid)" stroke-dasharray="2 2" stroke-width="1">
      <line x1="0" y1="46" x2="584" y2="46"/><line x1="0" y1="92" x2="584" y2="92"/>
      <line x1="0" y1="138" x2="584" y2="138"/><line x1="0" y1="184" x2="584" y2="184"/>
      <line x1="0" y1="230" x2="584" y2="230"/>
      <line x1="74" y1="0" x2="74" y2="279"/><line x1="148" y1="0" x2="148" y2="279"/>
      <line x1="220" y1="0" x2="220" y2="279"/><line x1="292" y1="0" x2="292" y2="279"/>
      <line x1="366" y1="0" x2="366" y2="279"/><line x1="438" y1="0" x2="438" y2="279"/>
      <line x1="510" y1="0" x2="510" y2="279"/>
    </g>
    <polygon fill="url(#area)" points="0,52 22,90 32,74 56,97 69,144 90,160 94,176 101,180 106,104 134,128 137,159 156,163 163,137 169,150 178,124 185,134 206,73 207,126 227,101 231,146 241,140 261,184 275,177 291,193 292,164 302,171 327,129 331,155 349,165 369,189 386,216 400,199 406,218 416,205 438,215 445,226 452,229 459,224 466,231 472,229 490,189 505,231 510,209 521,220 545,193 584,117 584,279 0,279"/>
    <g fill="none" stroke-width="1.3">
      <polyline stroke="var(--gain)" points="0,52 22,90 32,74 56,97 69,144 90,160 94,176 101,180 106,104 134,128 137,159 156,163 163,137 169,150 178,124 185,134 206,73 207,126 227,101 231,146 241,140 261,184 275,177"/>
      <polyline stroke="var(--loss)" points="275,177 291,193"/>
      <polyline stroke="var(--gain)" points="291,193 292,164 302,171 327,129 331,155 349,165 369,189"/>
      <polyline stroke="var(--loss)" points="369,189 386,216 400,199 406,218 416,205 438,215 445,226 452,229 459,224 466,231 472,229 490,189 505,231 510,209 521,220 545,193"/>
      <polyline stroke="var(--gain)" points="545,193 584,117"/>
    </g>
  </svg>
  <span class="year" style="left:605px">2014</span>
  <span class="year" style="left:1058px">2019</span>

  <section class="stats">
    <div class="stats__head">Stats</div>
    <div class="stats__table">
      <div class="stats__row">Stat 1 <span class="stats__value gain">0.5</span></div>
      <div class="stats__row">Stat 2 <span class="stats__value loss">-3</span></div>
      <div class="stats__row">Stat 3 <span class="stats__value gain">30%</span></div>
    </div>
  </section>
</body>
</html>
```